Business Card Design and Stationary design for consulting firm

Harbourline Sourcing are looking for a new business card design and a design for their A4 letterhead / A4 invoices.

We are seeking to heavily increase our brand awareness and require a business card that's professional in appearance but also shows flare and innovation. A card design that people will remember.

About Us
Harbourline Sourcing are `The Sourcing Crew’.
Our mission is to be one of Australia’s greatest companies. Our aim is to help our customers achieve the best result from their purchasing experience.

Our Requirement:
• IMPACT! IMPACT! IMPACT!
• BUSINESS & PROFESSIONAL LOOKING

• Our business colours are orange, blue and green (See the logo attached).

We have provided an Art Design specification (attached) that needs to be followed for you to win the design. This also has the font, which is used on the logo.

We are after a two sided business card

Side One should have the:
The company Logo
The Sourcing Crew
www.harbourlinesourcing.com.au
Procure | Personnel | Probity & Privacy
Sydney | Melbourne | Adelaide | Brisbane

Side Two
Logo (optional)
Harbourline Sourcing (optional)
Employee details (details listed below)

The above format is our preferred option, but if you think you can come up with something better, feel free to put it forward.

We are leaving the design up to you, but it must incorporate the logo.

We will need a template that we can change the employee details on, as we will be adding more staff over the coming months.

The details below are for one employee per card with the same design.
------------------------

Employee Details:

Marcus Del Arroyo MBA, MMgmtStratProc
Principal Consultant
0491 372 618
Marcus@harbourlinesourcing.com.au

Brianna Tolley
Consulting Manager
0462 915 308
Brianna@harbourlinesourcing.com.au

Our website is www.harbourlinesourcing.com.au

The Letterhead / invoice needs to incorporate:
the company Logo
The Sourcing Crew
Sydney | Melbourne | Adelaide | Brisbane but otherwise the design is over to you.

This file needs to be delivered in word format as other detail will be added to the documents.

We look forward to you award winning designs. If you require any further information please feel free to contact us.

Regards
Harbourline Sourcing

Target Market(s)

Our Target market is companies with 80+ employees. The market we segment is heavily male based, between the ages of 35-55 years of age.

Industry/Entity Type

Consulting

Contact Information for Business Card

See Project Description

Font styles to use
Other font styles liked:
• See Art Specification

Requirements
Must have
• Company Colours, See Project Description
Should not have
• Be outside the Art specification guidelines

```html
<!DOCTYPE html>
<html lang="en">
<head>
<meta charset="utf-8">
<title>Harbourline Sourcing – Business Card</title>
<link rel="stylesheet" href="https://fonts.googleapis.com/css2?family=Arimo:ital,wght@0,400;0,700;1,400&display=swap">
<style>
  :root {
    --paper: #ffffff;
    --ink: #111111;
    --web-band: #b4c6aa;
    --web-ink: #1a2a12;
    --hero-blue: #1c3a9a;
    --hero-green: #3b6a34;
    --hero-dark: #1d1d1d;
    --hero-red: #a0141a;
    --logo-ink: #ffffff;
  }
  html, body {
    margin: 0;
    padding: 0;
    overflow: hidden;
    background: var(--paper);
  }
  .card {
    position: relative;
    width: 1200px;
    height: 690px;
    background: var(--paper);
    font-family: "Arimo", Arial, sans-serif;
    color: var(--ink);
    overflow: hidden;
  }
  .hero-band {
    position: absolute;
    left: 0; top: 0;
    width: 1200px;
    height: 232px;
    background: linear-gradient(90deg,
      var(--hero-blue) 0%,
      #234a78 25%,
      var(--hero-green) 50%,
      #2a3a28 65%,
      #5a3040 80%,
      var(--hero-red) 100%);
  }
  .brand-name {
    position: absolute;
    left: 88px;
    top: 112px;
    margin: 0;
    font-weight: 700;
    font-size: 44px;
    letter-spacing: 2px;
    color: var(--logo-ink);
    text-transform: uppercase;
    line-height: 1;
  }
  .person {
    position: absolute;
    left: 86px;
    top: 294px;
  }
  .person-name {
    margin: 0;
    font-weight: 700;
    font-size: 48px;
    line-height: 1;
    text-transform: uppercase;
  }
  .credentials {
    font-weight: 400;
    font-style: italic;
    font-size: 30px;
    text-transform: none;
  }
  .role {
    margin: 8px 0 0;
    font-size: 35px;
    line-height: 1.1;
  }
  .contact {
    position: absolute;
    right: 85px;
    top: 458px;
    text-align: right;
    font-size: 37px;
    line-height: 47px;
  }
  .contact p { margin: 0; }
  .web-band {
    position: absolute;
    left: 0;
    top: 598px;
    width: 1200px;
    height: 59px;
    background: var(--web-band);
  }
  .web-address {
    position: absolute;
    right: 85px;
    top: 10px;
    margin: 0;
    font-size: 35px;
    line-height: 40px;
    color: var(--web-ink);
  }
</style>
</head>
<body>
  <main class="card">
    <div class="hero-band" role="img" aria-label="Woven geometric pattern fading from blue through green to red"></div>
    <p class="brand-name">Harbourline Sourcing</p>

    <section class="person">
      <h1 class="person-name">Marcus Del Arroyo <span class="credentials">MBA, MMgmtStratProc</span></h1>
      <p class="role">Principal Consultant</p>
    </section>

    <section class="contact">
      <p class="phone">0491 372 618</p>
      <p class="email">marcus@harbourlinesourcing.com.au</p>
    </section>

    <footer class="web-band">
      <p class="web-address">www.harbourlinesourcing.com.au</p>
    </footer>
  </main>
</body>
</html>
```